依頼詳細
最近、全国高校用教科書を編集しています。この度、これに対応した『テキスト』を関連編集しています。全部で16 unitありますが、設問のパターンはほとんど同じものです。ですから、『unit1』を対象に、6ページの基本編集レイアウトの作成を依頼したいのです。よろしくお願いします。
記載項目
『unit1』の原稿は添付いたします。
希望イメージ
シンプル 複雑
単色 カラフル
暗い 明るい
日常 高級
遊び心 厳粛
未来的 伝統的
女性的 男性的
希望する色
納品ファイル
• 高解像度JPG (.jpg)
• イラストレーター形式 (.ai)
補足説明
■ 選んだ理由

全ページのバランスが最もとれており、見本ページにふさわしかったので、本提案を当選として選びました。

■ 提案者全員のお礼・コメント

お盆休みの中、たくさんの御提案をいただきまして、大変感謝しております。当社は出版社ですから、依頼事項が続きます。今後とも、よろしくお願い申し上げます。

```html
<!DOCTYPE html>
<html lang="ja">
<head>
<meta charset="utf-8">
<title>Unit 1 Kenneth, This Is Oliver</title>
<link href="https://fonts.googleapis.com/css2?family=Noto+Sans+JP:wght@400;700;900&family=Noto+Serif+JP:wght@400;600&display=swap" rel="stylesheet">
<style>
:root{
  --ink:#1a1a1a;
  --paper:#ffffff;
  --band:#d9d9d9;
  --letter:#8a8a8a;
  --rule:#333333;
}
*{margin:0;padding:0;box-sizing:border-box}
html,body{width:849px;height:1200px;overflow:hidden;background:var(--paper)}
body{position:relative;color:var(--ink);font-family:"Noto Serif JP",serif;font-size:16px}
.abs{position:absolute}
.unit-badge{left:40px;top:58px;width:78px;height:78px;border-radius:50%;background:var(--ink);color:var(--paper);
  font-family:"Noto Sans JP",sans-serif;font-weight:900;text-align:center;line-height:1}
.unit-badge .label{display:block;font-size:15px;margin-top:14px;letter-spacing:1px}
.unit-badge .num{display:block;font-size:34px;margin-top:2px}
.unit-title{left:132px;top:66px;font-family:"Noto Sans JP",sans-serif;font-weight:900;font-size:34px;letter-spacing:.3px}
.title-rule{left:108px;top:122px;width:700px;height:4px;background:var(--rule)}
.source{right:42px;top:140px;font-family:"Noto Sans JP",sans-serif;font-weight:700;font-size:18px}
.skill-band{left:40px;top:180px;width:440px;height:34px;background:var(--band);font-family:"Noto Sans JP",sans-serif;
  font-weight:700;font-size:18px;line-height:34px;padding-left:12px}
.score-box{left:480px;top:172px;width:330px;height:50px;border:1.5px solid var(--ink)}
.score-box .cap{position:absolute;left:6px;top:3px;font-family:"Noto Sans JP",sans-serif;font-size:9px}
.score-box svg{position:absolute;right:0;top:0}
.sec-letter{font-family:"Noto Sans JP",sans-serif;font-weight:900;font-size:60px;color:var(--letter);line-height:1}
.instr{font-size:15px;line-height:28px;width:680px}
.q{font-size:16px;line-height:28px}
.q .n{display:inline-block;width:50px}
.ex{font-size:17px}
.ex u{text-underline-offset:3px}
.dot{width:15px;height:15px;border-radius:50%;background:var(--ink)}
.tip{left:70px;top:985px;width:720px;font-size:15px;line-height:28px}
.tip .lead{font-family:"Noto Serif",serif}
</style>
</head>
<body>
<div class="abs unit-badge"><span class="label">UNIT</span><span class="num">1</span></div>
<div class="abs unit-title">Kenneth, This Is Oliver</div>
<div class="abs title-rule"></div>
<div class="abs source">Oliver Small</div>

<div class="abs skill-band">□ Listening Skills</div>
<div class="abs score-box"><span class="cap">氏名</span>
  <svg width="80" height="48" viewBox="0 0 80 48"><line x1="60" y1="42" x2="76" y2="8" stroke="#1a1a1a" stroke-width="1.5"/></svg>
</div>

<div class="abs sec-letter" style="left:62px;top:240px">A</div>
<p class="abs instr" style="left:128px;top:250px">CD を聴き、空所を埋めながら、強勢アクセントに注意しながら、会話練習をしましょう。</p>
<div class="abs q" style="left:140px;top:292px">
  <p><span class="n">（1）</span>a. (How) are things with you?</p>
  <p><span class="n"></span>b. I'm getting (along) very well, thank you.</p>
</div>
<div class="abs q" style="left:140px;top:354px">
  <p><span class="n">（2）</span>a. (What) do you (do)?</p>
  <p><span class="n"></span>b. I'm a (high) (school) (teacher).</p>
</div>
<div class="abs q" style="left:140px;top:414px">
  <p><span class="n">（3）</span>a. (Where) do you (live)?</p>
  <p><span class="n"></span>b. I live (in) Minami-ku.</p>
</div>
<div class="abs q" style="left:140px;top:476px">
  <p><span class="n">（4）</span>a. (What) is your (favorite) subject?</p>
  <p><span class="n"></span>b. I like Japanese and (mathematics) best.</p>
</div>

<div class="abs sec-letter" style="left:62px;top:548px">B</div>
<p class="abs instr" style="left:128px;top:556px">CD を聴き、次の英文をリピートしてみましょう。その際、強弱のリズムに気をつけましょう。下線部要素（主語名詞、本動詞、目的語名詞）は強勢アクセント●が付与され、強く発音されます。</p>

<div class="abs q" style="left:140px;top:674px">（5）</div>
<div class="abs ex" style="left:190px;top:674px">a.&nbsp;&nbsp;<u>Dogs</u></div>
<div class="abs ex" style="left:470px;top:674px"><u>bite</u></div>
<div class="abs ex" style="left:644px;top:674px"><u>bones</u>.</div>
<div class="abs dot" style="left:222px;top:718px"></div>
<div class="abs dot" style="left:480px;top:718px"></div>
<div class="abs dot" style="left:662px;top:718px"></div>

<div class="abs ex" style="left:190px;top:772px">b.&nbsp;&nbsp;The <u>dogs</u></div>
<div class="abs ex" style="left:362px;top:772px">will</div>
<div class="abs ex" style="left:470px;top:772px"><u>bite</u></div>
<div class="abs ex" style="left:612px;top:772px">the <u>bones</u>.</div>
<div class="abs dot" style="left:270px;top:815px"></div>
<div class="abs dot" style="left:480px;top:815px"></div>
<div class="abs dot" style="left:662px;top:815px"></div>

<div class="abs ex" style="left:190px;top:874px">c.&nbsp;&nbsp;The <u>dogs</u></div>
<div class="abs ex" style="left:342px;top:874px">will have <u>bitten</u></div>
<div class="abs ex" style="left:612px;top:874px">the <u>bones</u>.</div>
<div class="abs dot" style="left:270px;top:918px"></div>
<div class="abs dot" style="left:458px;top:918px"></div>
<div class="abs dot" style="left:662px;top:918px"></div>

<p class="abs tip"><span class="lead">Listening Tip:</span> 内容語である名詞、動詞、形容詞には、強勢アクセントが付与され、一方、機能語である代名詞、助動詞、冠詞などには、強勢アクセントが付与されず、弱く発音される場合が多い。</p>
</body>
</html>
```